Wren Renovation Collective Postcard Design Project

I'm a General Contractor specializing in luxury residential remodeling.

THIS IS AN EDDM POSTCARD. THE ENTIRE BACK SIDE OF THE CARD WILL BE USED.

I FORGOT TO MENTION THIS IN MY ORIGINAL BRIEF.

Target Market(s)

OLD, rich people so please make sure the fonts are clear and crisp.

Font styles to use
Sans Serif

```html
<!DOCTYPE html>
<html lang="en">
<head>
<meta charset="utf-8">
<title>Wren Renovation Collective – Flyer and Postcard</title>
<link href="https://fonts.googleapis.com/css2?family=Nunito:wght@400;600;700;800;900&family=Oswald:wght@500&display=swap" rel="stylesheet">
<style>
  :root{
    --red:#d71920; --dark-red:#a8141b; --maroon:#7e1a1f; --salmon:#ea6868; --pink:#e0405a;
    --ink:#1c1c1c; --charcoal:#2b2b2b; --paper:#ffffff; --bg:#e6e6e6; --muted:#6b6b6b;
  }
  *{margin:0;padding:0;box-sizing:border-box}
  html,body{width:928px;height:1200px;overflow:hidden;background:var(--bg);font-family:'Nunito',sans-serif}
  .canvas{position:relative;width:928px;height:1200px}

  /* Flyer front */
  .flyer{position:absolute;left:24px;top:322px;width:370px;height:556px;background:var(--paper);overflow:hidden;box-shadow:0 6px 14px rgba(0,0,0,.25)}
  .flyer .stripe{position:absolute;left:0;top:0;width:100%;height:8px}
  .flyer .brand{position:absolute;top:38px;width:100%;display:flex;justify-content:center;align-items:center;gap:8px}
  .brand-mark{width:14px;height:14px;background:var(--red);flex:none}
  .brand-name{font-weight:800;color:var(--red);font-size:19px}
  .tagline{position:absolute;width:100%;text-align:center;color:var(--ink);line-height:1.2}
  .flyer .tagline{top:122px;font-size:15.5px}
  .tagline b{color:var(--red);font-weight:800}
  .tagline small{display:block;font-size:12px}
  .core-value{position:absolute;top:188px;left:50%;transform:translateX(-50%);border:1.5px solid #cfcfcf;padding:1px 8px;color:var(--red);font-weight:900;font-size:15.5px;letter-spacing:.3px}
  .flyer-photo{position:absolute;left:0;top:222px;width:100%;height:334px;background:linear-gradient(180deg,#b9b9b9 0%,#8d8d8d 30%,#5a5a5a 60%,#262626 100%)}
  .values{position:absolute;left:0;top:214px}
  .values text{font-family:'Nunito',sans-serif;font-weight:900;fill:#fff;font-size:6.5px;text-anchor:middle}
  .contractor{position:absolute;top:358px;width:100%;text-align:center;font-family:'Oswald',sans-serif;font-weight:500;color:var(--red);font-size:25px}
  .services{position:absolute;top:402px;width:100%;text-align:center;color:#fff;font-size:10px;line-height:1.35}
  .flyer .phone{position:absolute;top:430px;width:100%;text-align:center;color:#fff;font-weight:900;font-size:29px;line-height:1.2}
  .web{color:#fff;font-weight:700}
  .web b{color:var(--red);font-weight:800}
  .flyer .web{position:absolute;top:465px;width:100%;text-align:center;font-size:11.5px}
  .license{position:absolute;top:490px;left:50%;transform:translateX(-50%);border:1px solid #bbb;color:#eee;font-size:10px;padding:2px 7px;white-space:nowrap}
  .flip-note{position:absolute;width:100%;display:flex;justify-content:center;align-items:center;gap:6px;color:#fff;font-size:8px}
  .flip-note::before,.flip-note::after{content:"";width:40px;height:1px;background:#ddd}
  .flyer .flip-note{top:520px}
  .flyer .bottom-stripe{position:absolute;left:0;bottom:0;width:100%;height:6px;background:var(--red)}

  /* Postcard back */
  .postcard{position:absolute;left:392px;top:450px;width:520px;height:346px;background:var(--paper);overflow:hidden;box-shadow:0 6px 14px rgba(0,0,0,.25)}
  .promo{position:absolute;left:0;top:0;width:290px;height:346px}
  .promo-photo{position:absolute;left:0;top:40px;width:290px;height:260px;background:linear-gradient(160deg,#c9b28d 0%,#e9dfcf 35%,#b49a7a 60%,#3c3028 100%)}
  .promo .tagline{top:12px;font-size:12px}
  .promo .tagline small{font-size:9px}
  .promo-bar{position:absolute;left:0;top:290px;width:290px;height:56px;background:var(--charcoal)}
  .promo .phone{position:absolute;left:32px;top:286px;color:#fff;font-weight:900;font-size:28px}
  .promo .web{position:absolute;left:32px;top:318px;font-size:12px}
  .promo .flip-note{top:334px;left:0;width:auto;padding-left:62px;font-size:7.5px}
  .promo .flip-note::before{display:none}
  .mail-side .brand{position:absolute;left:304px;top:36px;width:124px;display:flex;align-items:center;gap:6px}
  .mail-side .brand-name{font-size:11px;line-height:1.15}
  .mail-side .brand-mark{width:10px;height:10px}
  .stamp{position:absolute;right:16px;top:26px;width:64px;height:58px;border:1px solid #9a9a9a}
  .address-line{position:absolute;left:330px;width:172px;height:1px;background:#8a8a8a}
</style>
</head>
<body>
<div class="canvas">

  <section class="flyer">
    <svg class="stripe" viewBox="0 0 370 8" preserveAspectRatio="none"><polygon points="0,0 184,0 176,8 0,8" fill="#d71920"/><polygon points="184,0 370,0 370,8 176,8" fill="#111"/></svg>
    <div class="brand"><span class="brand-mark"></span><span class="brand-name">Wren Renovation Collective</span></div>
    <p class="tagline">Remodeling <b>Luxury Homes</b> &amp; <b>Building</b><br><b>Lasting Relationships</b><small>Since 1995</small></p>
    <div class="core-value">OUR CORE VALUE</div>
    <div class="flyer-photo" role="img" aria-label="Photo of a bright, modern luxury home interior"></div>

    <svg class="values" width="370" height="160" viewBox="0 0 370 160">
      <g>
        <polygon points="47,6 93,52 47,98 1,52" fill="#d71920"/>
        <polygon points="139,6 185,52 139,98 93,52" fill="#ea6868"/>
        <polygon points="230,6 276,52 230,98 184,52" fill="#7e1a1f"/>
        <polygon points="322,6 368,52 322,98 276,52" fill="#d71920"/>
        <polygon points="93,52 139,98 93,144 47,98" fill="#a8141b"/>
        <polygon points="185,52 231,98 185,144 139,98" fill="#e0405a"/>
        <polygon points="276,52 322,98 276,144 230,98" fill="#c8102e"/>
      </g>
      <g fill="#fff">
        <circle cx="47" cy="36" r="5"/>
        <rect x="134" y="32" width="10" height="10" rx="2"/>
        <rect x="224" y="32" width="12" height="9"/>
        <rect x="313" y="36" width="4" height="3"/><rect x="320" y="36" width="11" height="3"/><rect x="313" y="42" width="4" height="3"/><rect x="320" y="42" width="11" height="3"/>
        <polygon points="93,77 103,82 93,87 83,82"/>
        <circle cx="185" cy="80" r="5"/>
        <circle cx="276" cy="80" r="5"/>
      </g>
      <text x="47" y="55">THE</text><text x="47" y="63">CREATIVE</text><text x="47" y="71">PROCESS</text>
      <text x="139" y="58">INTEGRITY</text>
      <text x="230" y="52">WORKS CLASS</text><text x="230" y="60">CUSTOMER</text><text x="230" y="68">SERVICE</text>
      <text x="322" y="58">CRAFTSMANSHIP</text>
      <text x="93" y="98">EDUCATING</text><text x="93" y="106">OUR</text><text x="93" y="114">CLIENTS</text>
      <text x="185" y="104">HAVING FUN</text>
      <text x="276" y="104">QUALITY</text>
    </svg>

    <h1 class="contractor">Daniel Wren, General Contractor</h1>
    <p class="services">All phases of Residential remodeling<br>partial &amp; large scale remodeling complimentary design service</p>
    <p class="phone">480-555-0142</p>
    <p class="web">www.<b>WrenRenovationCollective</b>.com</p>
    <p class="license">Licensed / Bonded / Insured #418306</p>
    <p class="flip-note">Please view other side</p>
    <div class="bottom-stripe"></div>
  </section>

  <section class="postcard">
    <div class="promo">
      <div class="promo-photo" role="img" aria-label="Photo of a luxury living room with cream sofa, round coffee table and flowers"></div>
      <svg style="position:absolute;left:0;top:0" width="290" height="346" viewBox="0 0 290 346">
        <polygon points="0,0 290,0 290,46 145,88 0,46" fill="#fff"/>
        <polygon points="0,46 145,88 290,46 290,56 145,100 0,56" fill="#d71920"/>
        <polygon points="0,220 0,290 290,290 290,270 120,226" fill="#d71920"/>
        <polygon points="0,250 0,290 110,290" fill="#a8141b"/>
      </svg>
      <p class="tagline">Remodeling <b>Luxury Homes</b> &amp; <b>Building</b><br><b>Lasting Relationships</b><small>Since 1995</small></p>
      <div class="promo-bar"></div>
      <p class="phone">480-555-0142</p>
      <p class="web">www.<b>WrenRenovationCollective</b>.com</p>
      <p class="flip-note">Please view other side</p>
    </div>
    <div class="mail-side">
      <div class="brand"><span class="brand-mark"></span><span class="brand-name">Wren Renovation<br>Collective</span></div>
      <div class="stamp"></div>
      <div class="address-line" style="top:206px"></div>
      <div class="address-line" style="top:240px"></div>
      <div class="address-line" style="top:272px"></div>
    </div>
  </section>

</div>
</body>
</html>
```